Business Card for a Floral & Decorating Business

I would like to take my current logo and create a better business card. I am looking for elegance as I am a florist and event decorator. My logo has multiple colour options. I like colours like green, purple, pink and orange, I think I would like a white card, open to black back ground. I want it to feel elegant and romantic. I like metallic lettering that maybe is indented in the paper, I also like glossy paper. I have a full logo already as well as a badge. I have attached both in multiple colours.m
Updates

Need extra days to review

Target Market(s)

Weddings, special events, floral customers

Industry/Entity Type

Floral and decorating

Contact Information for Business Card

Phone number, email, instagram, facebook, title, name, logo

Font styles to use
Script

Requirements
Nice to have
• Elegant

```html
<!DOCTYPE html>
<html lang="en">
<head>
<meta charset="utf-8">
<title>Marlow Ashby — Business Card</title>
<link rel="stylesheet" href="https://fonts.googleapis.com/css2?family=Playfair+Display:wght@400&family=Pinyon+Script&display=swap">
<style>
  :root {
    --backdrop: #e4e4e4;
    --blush: #e8b9aa;
    --ink: #1c1414;
    --night: #0f0f0f;
    --paper: #ffffff;
  }
  * { box-sizing: border-box; margin: 0; padding: 0; }
  html, body {
    width: 1200px;
    height: 1101px;
    overflow: hidden;
    background: var(--backdrop);
  }
  .canvas {
    position: relative;
    width: 1200px;
    height: 1101px;
  }
  .card {
    position: absolute;
    top: 265px;
    width: 308px;
    height: 540px;
  }
  .card--front { left: 243px; background: var(--blush); color: var(--ink); }
  .card--back { left: 640px; background: var(--night); color: var(--blush); }

  .badge {
    position: absolute;
    left: 60px;
    top: 53px;
    width: 188px;
    height: 188px;
    border: 1px solid var(--ink);
    border-radius: 50%;
    display: flex;
    align-items: center;
    justify-content: center;
  }
  .badge__name {
    font-family: "Playfair Display", serif;
    font-size: 15px;
    letter-spacing: 0.2em;
    text-transform: uppercase;
    text-align: center;
    line-height: 1.5;
  }

  .signature {
    position: absolute;
    left: 0;
    top: 280px;
    width: 100%;
    font-family: "Pinyon Script", cursive;
    font-size: 52px;
    line-height: 0.9;
    color: var(--ink);
  }
  .signature__first { display: block; padding-left: 46px; }
  .signature__last { display: block; padding-left: 118px; }

  .contact {
    position: absolute;
    left: 0;
    top: 414px;
    width: 100%;
    text-align: center;
    font-family: "Playfair Display", serif;
    font-size: 14.5px;
    letter-spacing: 0.08em;
    line-height: 21.5px;
  }

  .monogram-name {
    position: absolute;
    left: 0;
    top: 150px;
    width: 100%;
    text-align: center;
    font-family: "Playfair Display", serif;
    font-size: 46px;
    line-height: 1.15;
    color: var(--blush);
  }
  .social-handle {
    position: absolute;
    left: 0;
    top: 462px;
    width: 100%;
    text-align: center;
    font-family: "Playfair Display", serif;
    font-size: 15px;
    letter-spacing: 0.08em;
    color: var(--paper);
  }
</style>
</head>
<body>
  <main class="canvas">
    <section class="card card--front" aria-label="Card front">
      <div class="badge">
        <p class="badge__name">Marlow<br>Ashby</p>
      </div>
      <h1 class="signature">
        <span class="signature__first">marlow</span>
        <span class="signature__last">ashby</span>
      </h1>
      <address class="contact" style="font-style: normal;">
        (555) 318 2046<br>
        hello@marlowashby.com<br>
        marlowashby.com
      </address>
    </section>

    <section class="card card--back" aria-label="Card back">
      <p class="monogram-name">Marlow<br>Ashby</p>
      <p class="social-handle">@marlowashby</p>
    </section>
  </main>
</body>
</html>
```